Harbor Wonder Hour - A magic website for a monthly modern magic show

Looking to build a website to promote my new monthly magic show

Sites like this. https://velvetloftshow.example/ https://brasslanterntricks.example/

Target Market(s)

18-65 year old men and women who enjoy live entertainment especially magic

Industry/Entity Type

Entertainment

Coding

Coded - Design and coding required

Number of Pages Required

3 page

Colors

Designer to choose colors to be used in the design.

Requirements
Must have
• Wanting a wordpress site.
• Contact form, media section for photos and videos to be posted.
• A “reviews/testimonials” section.

```html
<!DOCTYPE html>
<html lang="en">
<head>
<meta charset="UTF-8">
<title>Harbor Wonder Hour — Contact</title>
<link rel="stylesheet" href="https://fonts.googleapis.com/css2?family=Poppins:wght@400;500;600;700;800&display=swap">
<style>
  :root {
    --bg-deep: #141416;
    --bg-mid: #2a2b2e;
    --card: #232323;
    --button: #1e1e1e;
    --text: #ffffff;
    --text-soft: #e4e4e4;
    --line: #6a6a6a;
    --dot: #8a8a8a;
  }
  * { box-sizing: border-box; margin: 0; padding: 0; }
  html, body {
    width: 1200px; height: 800px; overflow: hidden;
    background: var(--bg-deep);
    font-family: "Poppins", sans-serif;
    color: var(--text);
  }
  .page { position: relative; width: 1200px; height: 800px; overflow: hidden; }
  .backdrop {
    position: absolute; inset: 0;
    background:
      radial-gradient(ellipse 420px 300px at 420px 180px, rgba(90,92,98,0.45), transparent 70%),
      radial-gradient(ellipse 500px 260px at 950px 120px, rgba(70,72,78,0.35), transparent 70%),
      linear-gradient(180deg, var(--bg-mid) 0%, #1c1d20 55%, var(--bg-deep) 100%);
  }
  .brand {
    position: absolute; left: 44px; top: 40px;
    font-size: 17px; font-weight: 800; letter-spacing: 0.2px;
  }
  .main-nav { position: absolute; right: 44px; top: 45px; display: flex; gap: 24px; }
  .main-nav a {
    color: var(--text); text-decoration: none;
    font-size: 11px; font-weight: 500;
  }
  .card {
    position: absolute; top: 193px; width: 504px; height: 415px;
    background: var(--card);
    text-align: center;
  }
  .testimonials { left: 74px; }
  .contact { left: 622px; }
  .card-title { font-size: 24px; font-weight: 700; letter-spacing: 0.2px; }
  .testimonials .card-title { margin-top: 91px; }
  .reviewer { margin-top: 38px; font-size: 13px; font-weight: 600; }
  .quote {
    margin: 16px auto 0; width: 410px;
    font-size: 11.5px; line-height: 22px; color: var(--text-soft);
  }
  .slider-dots { margin-top: 30px; display: flex; justify-content: center; gap: 8px; }
  .slider-dots span { width: 7px; height: 7px; border-radius: 50%; background: var(--dot); }
  .slider-dots span.active { background: var(--text); }
  .contact .card-title { margin-top: 37px; }
  .contact-form { margin: 30px 45px 0; text-align: left; }
  .field {
    display: block; border-bottom: 1px solid var(--line);
    font-size: 10px; font-weight: 400; padding-bottom: 4px;
    margin-bottom: 38px; color: var(--text-soft);
  }
  .send-button {
    display: block; margin: 4px auto 0; width: 162px; height: 36px;
    background: var(--button); border: none; color: var(--text);
    font-family: "Poppins", sans-serif; font-size: 10px; font-weight: 600; letter-spacing: 0.4px;
    box-shadow: 0 4px 10px rgba(0,0,0,0.35);
  }
  .social-list {
    position: absolute; left: 40px; top: 628px; list-style: none;
  }
  .social-list li { font-size: 9px; font-weight: 600; height: 37px; }
  .scroll-hint {
    position: absolute; left: 1143px; top: 676px;
    writing-mode: vertical-rl;
    font-size: 9.5px; font-weight: 500; letter-spacing: 0.4px;
  }
</style>
</head>
<body>
<div class="page">
  <div class="backdrop" role="img" aria-label="Dark moody photograph of a rain-wet street with a reflection in a puddle"></div>

  <div class="brand">NAME</div>
  <nav class="main-nav">
    <a href="#">TRICKS</a>
    <a href="#">CONTACT ME</a>
  </nav>

  <section class="card testimonials">
    <h2 class="card-title">WHAT THEY SAY</h2>
    <p class="reviewer">MARA ELLISON</p>
    <p class="quote">The Velvet Loft, in collaboration with cardhouse9, presents THE MAGICIAN, an intimate evening of magic, mystery, and deception. Starring Theo Marsh. Every Weekend.</p>
    <div class="slider-dots"><span></span><span class="active"></span><span></span></div>
  </section>

  <section class="card contact">
    <h2 class="card-title">CONTACT ME</h2>
    <form class="contact-form">
      <span class="field">YOUR NAME...</span>
      <span class="field">YOUR EMAIL...</span>
      <span class="field">YOUR SUBJECT...</span>
      <span class="field">YOUR MESSAGE...</span>
      <button type="button" class="send-button">SEND MESSAGE NOW</button>
    </form>
  </section>

  <ul class="social-list">
    <li>Gather</li>
    <li>Murmur</li>
    <li>Workly</li>
    <li>Folio</li>
  </ul>

  <div class="scroll-hint">SCROLL DOWN</div>
</div>
</body>
</html>
```